Business Card - Professional Minimalist - Double sided

We appreciate minimalist logo/web/collateral designs that allow design to tell a story. We want to relay a professional image/approach but throwing in a splash of modern when we’re able so long as it’s not distracting. Think 75% classic corporate, 25% modern. Open to black or white design, not sure which might look the best.

Target Market(s)

Senior executives or related government affairs contacts within the agriculture, energy, and defense industries (i.e., potential clients) but located outside of Washington, DC. Most potential clients based in DC with be familiar with both of us and our shared history.

Industry/Entity Type

Consulting

Contact Information for Business Card

Name: Derek M. Holloway
Title: Co-Founder & Partner
Address: 418 Linwood Terrace NE | Suite 2260 | Washington, D.C. 20017
Phone: (202) 555-0148
Email: Derek@BrimleyHolloway.example

Font styles to use
Serif

Colors

Designer to choose only greyscale colors for use in the design.

Requirements
Must have
• Name: Derek M. Holloway
Phone: (202) 555-0148

```html
<!DOCTYPE html>
<html lang="en">
<head>
<meta charset="utf-8">
<title>Brimley Holloway Group – Business Card</title>
<link rel="stylesheet" href="https://fonts.googleapis.com/css2?family=Source+Serif+4:wght@400;600&display=swap">
<style>
  :root {
    --page: #ffffff;
    --card-dark: #2a2a2a;
    --card-light: #ebebed;
    --ink-light: #f0f0f0;
    --ink-mark: #6e6e70;
    --ink-brand: #58585a;
    --serif: "Source Serif 4", Georgia, serif;
  }
  html, body {
    margin: 0;
    padding: 0;
    width: 1200px;
    height: 1200px;
    overflow: hidden;
    background: var(--page);
  }
  .canvas {
    position: relative;
    width: 1200px;
    height: 1200px;
    font-family: var(--serif);
  }
  .card {
    position: absolute;
    left: 239px;
    width: 730px;
    height: 417px;
  }
  .card--front {
    top: 130px;
    background: var(--card-dark);
    color: var(--ink-light);
  }
  .card--back {
    top: 660px;
    background: var(--card-light);
  }
  .front-brand {
    position: absolute;
    top: 35px;
    right: 36px;
    font-size: 10px;
    letter-spacing: 0.14em;
    text-transform: uppercase;
    color: var(--ink-mark);
    font-weight: 600;
  }
  .person {
    position: absolute;
    left: 35px;
    top: 196px;
  }
  .person__name {
    margin: 0;
    font-size: 35px;
    font-weight: 400;
    line-height: 1;
  }
  .person__title {
    margin: 4px 0 0;
    font-size: 17px;
    line-height: 1.2;
  }
  .contact {
    position: absolute;
    left: 35px;
    top: 310px;
    margin: 0;
    font-size: 17px;
    line-height: 22px;
    font-style: normal;
  }
  .contact span { display: block; }
  .brand {
    position: absolute;
    inset: 0;
    display: flex;
    align-items: center;
    justify-content: center;
    gap: 18px;
  }
  .brand__square {
    width: 46px;
    height: 46px;
    background: var(--ink-brand);
  }
  .brand__name {
    font-size: 31px;
    font-weight: 600;
    letter-spacing: 0.04em;
    text-transform: uppercase;
    color: var(--ink-brand);
  }
</style>
</head>
<body>
<main class="canvas">
  <section class="card card--front" aria-label="Card front">
    <div class="front-brand">Brimley Holloway Group</div>
    <div class="person">
      <h1 class="person__name">Derek M. Holloway</h1>
      <p class="person__title">Co-Founder &amp; Partner</p>
    </div>
    <address class="contact">
      <span>418 Linwood Terrace NE | Suite 2260 | Washington, D.C. 20017</span>
      <span>(202) 555-0148</span>
      <span>Derek@BrimleyHolloway.example</span>
    </address>
  </section>
  <section class="card card--back" aria-label="Card back">
    <div class="brand">
      <div class="brand__square"></div>
      <div class="brand__name">Brimley Holloway Group</div>
    </div>
  </section>
</main>
</body>
</html>
```